Clean and modern business cards

Looking for an updated business card design for my dental office “corvanta dental” . Looking for a modern clean / sleek design . I’m thinking black background but open to seeing other options . One side needs to have an appointment card . Card needs to have logo, dentist name , phone, email , address . I’ve attached couple of cards I thought were cool as well as my logo
Target Market(s)
Dental patients
Industry/Entity Type
Dentistry
Contact Information for Business Card
Phone email address

```html
<!DOCTYPE html>
<html lang="en">
<head>
<meta charset="utf-8">
<title>Corvanta Dental – Business Card</title>
<link rel="stylesheet" href="https://fonts.googleapis.com/css2?family=Barlow+Condensed:wght@300&family=Barlow+Semi+Condensed:wght@500;600&display=swap">
<style>
  :root {
    --page: #ffffff;
    --ink: #111111;
    --card-dark: #1b1a1c;
    --cyan: #08a6d9;
    --lime: #9ccb3a;
    --violet: #6b2a93;
    --white: #ffffff;
    --label-fill: #e6d9ea;
    --rule: #c9c9c9;
    --frame: #a9a9a9;
    --corner-green: #95c23d;
    --corner-purple: #7c3f98;
  }
  * { margin: 0; padding: 0; box-sizing: border-box; }
  html, body { width: 1200px; height: 1000px; overflow: hidden; background: var(--page); }
  body { position: relative; font-family: "Barlow Semi Condensed", Arial, sans-serif; color: var(--ink); }

  .card { position: absolute; left: 242px; width: 717px; height: 416px; }

  /* Front */
  .card-front {
    top: 54px;
    background:
      radial-gradient(ellipse 300px 260px at 0% 100%, rgba(156,203,58,1) 0%, rgba(156,203,58,.55) 40%, rgba(156,203,58,0) 100%),
      radial-gradient(ellipse 260px 300px at 0% 0%, rgba(8,166,217,1) 0%, rgba(8,166,217,.6) 35%, rgba(8,166,217,0) 100%),
      radial-gradient(ellipse 340px 300px at 100% 100%, rgba(107,42,147,1) 0%, rgba(107,42,147,.55) 40%, rgba(107,42,147,0) 100%),
      var(--card-dark);
    color: var(--white);
  }
  .brand { position: absolute; left: 40px; top: 112px; width: 158px; text-align: right; font-weight: 600; line-height: 1; }
  .brand-name { display: block; font-size: 33px; letter-spacing: .5px; }
  .brand-sub { display: block; font-size: 15px; letter-spacing: 3px; margin-top: 4px; }
  .dentist-name { position: absolute; top: 262px; left: 0; width: 100%; text-align: center; font-size: 32px; font-weight: 500; }
  .contact { position: absolute; top: 316px; left: 0; width: 100%; text-align: center; font-family: "Barlow Condensed", Arial, sans-serif; font-weight: 300; font-size: 16px; line-height: 25px; letter-spacing: .2px; }

  /* Back */
  .card-back { top: 531px; border: 1px solid var(--frame); background: var(--white); }
  .corner { position: absolute; width: 38px; height: 38px; }
  .corner-top { left: 0; top: 0; background: var(--corner-green); }
  .corner-bottom { right: 0; bottom: 0; background: var(--corner-purple); }
  .appointment-title { position: absolute; top: 68px; left: 0; width: 100%; text-align: center; font-size: 27px; font-weight: 500; }
  .appointment-table { position: absolute; left: 71px; top: 114px; width: 564px; height: 168px; border: 1px solid var(--rule); border-radius: 30px; overflow: hidden; }
  .row { position: absolute; left: 0; width: 100%; height: 84px; }
  .row-date { top: 0; border-bottom: 1px solid var(--rule); }
  .row-time { top: 84px; }
  .row-label { position: absolute; left: 0; top: 0; width: 91px; height: 100%; background: var(--label-fill); border-right: 1px solid var(--rule); display: flex; align-items: center; justify-content: center; font-size: 23px; font-weight: 500; padding-top: 8px; }
  .row-line { position: absolute; left: 109px; right: 18px; top: 41px; border-top: 1px dashed #8a8a8a; }
  .note { position: absolute; top: 336px; left: 0; width: 100%; text-align: center; font-size: 18px; font-weight: 500; line-height: 25px; }
</style>
</head>
<body>
  <section class="card card-front">
    <div class="brand">
      <span class="brand-name">CORVANTA</span>
      <span class="brand-sub">DENTAL</span>
    </div>
    <h1 class="dentist-name">Dr.Lucas Renfield</h1>
    <p class="contact">
      2840 MARLOW HWY , WINNIPEG , MB || (204) 555-0192<br>
      CORVANTAWPG.CA || CONTACT @CORVANTAWPG.CA
    </p>
  </section>

  <section class="card card-back">
    <span class="corner corner-top"></span>
    <span class="corner corner-bottom"></span>
    <h2 class="appointment-title">Your Next Appointment is :</h2>
    <div class="appointment-table">
      <div class="row row-date"><span class="row-label">Date</span><span class="row-line"></span></div>
      <div class="row row-time"><span class="row-label">Time</span><span class="row-line"></span></div>
    </div>
    <p class="note">* To cancel or reschedule please notify us at<br>least 48 hours to your sheduled appointment</p>
  </section>
</body>
</html>
```